Copper Lantern LLC Business Card

We need a business card design for a newco in Texas. We are a team of professionals who join start ups as founders and help launch their businesses, which are primarily related to food and beverage and the service side of the industry. We love local and craft and are partners in businesses in the local meat, BBQ and Burger, fine dining, and beverage alcohol businesses. Our specialty is finance and the business side of start ups, including assisting with capital raises as principals, not brokers. We do not currently have any logos or graphics for this entity. Our values include helping people succeed, rooting for the underdog, healthy food, the environment and being good citizens.

Target Market(s)

Everybody but also Angel Investors, CPAs, Bankers, Entrepreneurs

Industry/Entity Type

Business

Contact Information for Business Card

Fields for Business Name, Title, Email Address, Phone Number. Place to add mailing address and web domain later.

Font styles to use
Sans Serif

Colors

Designer to choose colors to be used in the design.

Requirements
Should not have
• Pictures of booze bottles or drinks thought there could be a social scene that does not strictly focus on those. No cows, cowboy hats or ranches. We are not a Wall Street type entity so no huge office buildings or skylines.

```html
<!DOCTYPE html>
<html lang="en">
<head>
<meta charset="utf-8">
<title>Copper Lantern LLC Business Card</title>
<link href="https://fonts.googleapis.com/css2?family=Lato:wght@400;700&display=swap" rel="stylesheet">
<style>
  :root {
    --backdrop: #e9e7e4;
    --card: #fbfbfa;
    --brand-red: #c8202f;
    --ink: #1d1d1d;
    --rule: #9a9a9a;
    --band-text: #ffffff;
  }
  html, body {
    margin: 0;
    padding: 0;
    width: 1200px;
    height: 780px;
    overflow: hidden;
    background: var(--backdrop);
    font-family: "Lato", Arial, sans-serif;
  }
  .canvas {
    position: relative;
    width: 1200px;
    height: 780px;
  }
  .card {
    position: absolute;
    left: 75px;
    top: 90px;
    width: 1050px;
    height: 600px;
    background: var(--card);
    box-shadow: 0 4px 18px rgba(0,0,0,0.18);
    overflow: hidden;
  }
  .brand {
    position: absolute;
    left: 70px;
    top: 160px;
    width: 360px;
    display: flex;
    align-items: center;
    gap: 18px;
  }
  .brand-dot {
    flex: none;
    width: 70px;
    height: 70px;
    border-radius: 50%;
    border: 3px solid var(--brand-red);
    box-sizing: border-box;
  }
  .brand-name {
    margin: 0;
    font-weight: 700;
    font-size: 40px;
    line-height: 1.1;
    color: var(--brand-red);
  }
  .divider {
    position: absolute;
    left: 468px;
    top: 60px;
    width: 1px;
    height: 330px;
    background: var(--rule);
  }
  .person {
    position: absolute;
    left: 545px;
    top: 60px;
  }
  .person-name {
    margin: 0;
    font-weight: 400;
    font-size: 38px;
    letter-spacing: 0.5px;
    color: var(--ink);
  }
  .person-title {
    margin: 2px 0 0;
    font-weight: 400;
    font-size: 32px;
    color: var(--brand-red);
  }
  .contacts {
    list-style: none;
    margin: 44px 0 0;
    padding: 0;
  }
  .contacts li {
    display: flex;
    align-items: center;
    gap: 14px;
    font-size: 26px;
    line-height: 38px;
    color: var(--ink);
  }
  .contacts svg {
    width: 22px;
    height: 22px;
    flex: none;
  }
  .band-rule {
    position: absolute;
    left: 0;
    right: 0;
    bottom: 108px;
    height: 4px;
    background: var(--ink);
  }
  .band {
    position: absolute;
    left: 0;
    right: 0;
    bottom: 0;
    height: 96px;
    background: var(--brand-red);
    display: flex;
    align-items: center;
    padding-left: 150px;
  }
  .address {
    margin: 0;
    font-size: 30px;
    color: var(--band-text);
    letter-spacing: 0.3px;
  }
</style>
</head>
<body>
<div class="canvas">
  <section class="card">
    <div class="brand">
      <span class="brand-dot"></span>
      <h1 class="brand-name">Copper Lantern LLC</h1>
    </div>

    <div class="divider"></div>

    <div class="person">
      <h2 class="person-name">DANIEL REYES</h2>
      <p class="person-title">Managing Director</p>
      <ul class="contacts">
        <li>
          <svg viewBox="0 0 24 24" aria-hidden="true"><path fill="#c8202f" d="M6.6 10.8a15 15 0 0 0 6.6 6.6l2.2-2.2a1 1 0 0 1 1-.25 11.4 11.4 0 0 0 3.6.57 1 1 0 0 1 1 1V20a1 1 0 0 1-1 1A17 17 0 0 1 3 4a1 1 0 0 1 1-1h3.5a1 1 0 0 1 1 1c0 1.25.2 2.45.57 3.57a1 1 0 0 1-.25 1z"/></svg>
          (01) 5550 1472
        </li>
        <li>
          <svg viewBox="0 0 24 24" aria-hidden="true"><path fill="#c8202f" d="M7 3h10v5H7zM4 9h16a2 2 0 0 1 2 2v6h-4v4H6v-4H2v-6a2 2 0 0 1 2-2zm4 7v3h8v-3z"/></svg>
          (01) 5550 1472
        </li>
        <li>
          <svg viewBox="0 0 24 24" aria-hidden="true"><path fill="#c8202f" d="M2 5h20v14H2zm2 2v.5l8 5 8-5V7z"/></svg>
          info@copperlantern.com
        </li>
        <li>
          <svg viewBox="0 0 24 24" aria-hidden="true"><circle cx="12" cy="12" r="9" fill="none" stroke="#c8202f" stroke-width="2"/><path d="M3 12h18M12 3c3 3 3 15 0 18M12 3c-3 3-3 15 0 18" fill="none" stroke="#c8202f" stroke-width="1.6"/></svg>
          www.copperlantern.com
        </li>
      </ul>
    </div>

    <div class="band-rule"></div>
    <div class="band">
      <p class="address">PO BOX 418 Lamar Blvd, 2nd street Austin ,USA</p>
    </div>
  </section>
</div>
</body>
</html>
```